Need a professional Facebook banner and app built that shows professionalism and continuity with our

I need a Facebook banner and app that reflect our website and professionalism. There should be continuity in our branding. Our website being developed is: http://tealpine.srvqk7-tz4.b9cloudly.com/wealth-management

```html
<!DOCTYPE html>
<html lang="en">
<head>
<meta charset="utf-8">
<title>Tealpine Wealth – Cover</title>
<link rel="stylesheet" href="https://fonts.googleapis.com/css2?family=Cinzel:wght@400&family=Libre+Baskerville&display=swap">
<style>
  :root {
    --stage-bg: #3a3a3a;
    --navy: #1e3d6d;
    --navy-deep: #17325c;
    --orange: #f7941d;
    --white: #ffffff;
    --photo-light: #cfcac2;
    --photo-mid: #8a8682;
    --photo-dark: #2d3340;
  }
  html, body {
    margin: 0;
    padding: 0;
    width: 1200px;
    height: 1200px;
    overflow: hidden;
    background: var(--stage-bg);
  }
  .stage {
    width: 1200px;
    height: 1200px;
    display: flex;
    align-items: center;
    justify-content: center;
  }
  .cover {
    display: block;
    width: 1200px;
    height: 457px;
    box-shadow: 0 4px 14px rgba(0,0,0,0.45);
  }
  .headline {
    font-family: "Cinzel", "Times New Roman", serif;
    fill: var(--orange);
  }
  .tagline {
    font-family: "Libre Baskerville", "Times New Roman", serif;
    fill: var(--white);
  }
  .brand-name {
    font-family: "Libre Baskerville", "Times New Roman", serif;
    fill: var(--navy);
  }
</style>
</head>
<body>
<main class="stage">
  <svg class="cover" viewBox="0 0 820 312" xmlns="http://www.w3.org/2000/svg">
    <defs>
      <linearGradient id="photoTone" x1="0" y1="0" x2="1" y2="1">
        <stop offset="0" stop-color="var(--photo-light)"/>
        <stop offset="0.5" stop-color="var(--photo-mid)"/>
        <stop offset="1" stop-color="var(--photo-dark)"/>
      </linearGradient>
    </defs>

    <rect class="cover-photo" x="0" y="0" width="560" height="312" fill="url(#photoTone)"
          role="img" aria-label="Photo of a businessman working on a laptop showing financial charts"/>

    <polygon class="accent-stripe" points="509,0 519,0 472,214 461,226" fill="var(--orange)"/>
    <polygon class="navy-panel" points="519,0 820,0 820,312 545,312 470,224" fill="var(--navy)"/>

    <polygon class="brand-tab-border" points="455,218 552,312 306,312" fill="var(--orange)"/>
    <polygon class="brand-tab" points="455,228 540,312 324,312" fill="var(--white)"/>

    <rect class="brand-mark" x="386" y="274" width="14" height="14" fill="var(--navy)"/>
    <text class="brand-name" x="405" y="286" font-size="12">Tealpine Wealth</text>

    <text class="headline" x="520" y="111" font-size="70" textLength="288" lengthAdjust="spacingAndGlyphs">ADVICE.</text>
    <text class="headline" x="522" y="157" font-size="47" textLength="282" lengthAdjust="spacingAndGlyphs">STRATEGIES.</text>
    <text class="headline" x="524" y="217" font-size="62" textLength="278" lengthAdjust="spacingAndGlyphs">RESULTS.</text>
    <text class="tagline" x="526" y="247" font-size="20" textLength="275" lengthAdjust="spacingAndGlyphs">A GUIDE TO YOUR MONEY</text>
  </svg>
</main>
</body>
</html>
```